Modern luxury trendy cosmetics label

Looking for a cosmetics packaging label design. We are looking for a professionel, modern and luxury look like Lorena Vasquel, Meadowkin Apothecary, Marigold Tessin, Gavin Albert Pruke, Zuna, Orvik + Dalle, Velumi, Sleepy Walrus, the plainfold, lumiere de sable.Name of product: Nordic Tulip Mask - Needle-Free Contour Ritual Ingredients that have scientific proof of anti aging: Cherry blossom extact, collegen, hyaluronic acid, coconut oil. Color of product itself: Pastel pink. Smell: Cherry blossom. Colors of label: simple and black and white or some subtle colors.

Target Market(s)

Women, luxury market, modern women, young and old women

Industry/Entity Type

Cosmetics

Font styles to use
Sans Serif

Colors

Designer to choose colors to be used in the design.

Requirements
Must have
• A modern look, professional, cosmetics, beauty, professional market, original

```html
<!DOCTYPE html>
<html lang="en">
<head>
<meta charset="utf-8">
<title>Ondira – Nordic Tulip Mask Label</title>
<link href="https://fonts.googleapis.com/css2?family=Questrial&family=Oswald:wght@500&family=Lato:wght@300&display=swap" rel="stylesheet">
<style>
  :root {
    --backdrop: #ead0c4;
    --label: #ffffff;
    --ink: #141414;
    --ink-soft: #3a3a3a;
  }
  html, body {
    margin: 0;
    padding: 0;
    width: 1199px;
    height: 1200px;
    overflow: hidden;
    background: var(--backdrop);
  }
  .canvas {
    position: relative;
    width: 1199px;
    height: 1200px;
  }
  .label {
    position: absolute;
    left: 294px;
    top: 320px;
    width: 611px;
    height: 560px;
    background: var(--label);
    box-shadow: 0 2px 18px rgba(120, 80, 70, 0.12);
    text-align: center;
    color: var(--ink);
  }
  .label > * {
    position: absolute;
    left: 0;
    right: 0;
    margin: 0;
  }
  .brand {
    top: 88px;
    font-family: "Questrial", sans-serif;
    font-size: 76px;
    line-height: 1;
    letter-spacing: 1px;
    font-weight: 400;
  }
  .product-name {
    top: 274px;
    font-family: "Oswald", sans-serif;
    font-weight: 500;
    font-size: 38px;
    line-height: 1;
    letter-spacing: 7px;
    padding-left: 7px;
  }
  .product-type {
    top: 333px;
    font-family: "Lato", sans-serif;
    font-weight: 300;
    font-size: 24px;
    line-height: 1;
    letter-spacing: 3px;
    color: var(--ink-soft);
  }
  .scent {
    top: 424px;
    font-family: "Oswald", sans-serif;
    font-weight: 500;
    font-size: 18px;
    line-height: 1;
    letter-spacing: 4px;
  }
  .volume {
    top: 510px;
    font-family: "Oswald", sans-serif;
    font-weight: 500;
    font-size: 15px;
    line-height: 1;
    letter-spacing: 3px;
  }
</style>
</head>
<body>
  <main class="canvas">
    <section class="label">
      <h1 class="brand">ondira</h1>
      <h2 class="product-name">NORDIC TULIP</h2>
      <p class="product-type">MASK</p>
      <p class="scent">CHERRY BLOSSOM</p>
      <p class="volume">100ML</p>
    </section>
  </main>
</body>
</html>
```